Harborline Open Cinema Gathering 20th Annual Poster

September 2017 will to the 20th Annual Harborline Open Cinema Gathering. We have a new logo and need a new modern stylish poster designed. One that shows creativity, imagination, style and class. Think outside the box. Modern and new.

Dates are: September 7th - 13th 2017

Our tagline:
"Something for Everyone from Around the World"

Target Market(s)

film festival goings - 35 - 70 age range - 58% female 42% males - movie lovers - movie goers

Industry/Entity Type

Movie

Font styles to use
Script

Requirements
Must have
• modern style celebrating 20 years - cool design - chic and stylish - upscale - high society - think Abstract
Nice to have
• thinking outside the box - not just simple film reel - think Abstract! Not just your standard film items. Creative in your idea and design
Should not have
• no CLIP ART

```html
<!DOCTYPE html>
<html lang="en">
<head>
<meta charset="utf-8">
<title>Harborline Open Cinema Gathering – 20th Annual Poster</title>
<link rel="stylesheet" href="https://fonts.googleapis.com/css2?family=Josefin+Sans:wght@300;600&family=Parisienne&display=swap">
<style>
  :root {
    --navy-deep: #1e2160;
    --navy-mid: #34387a;
    --navy-soft: #4c4f8f;
    --wood-tint: #5a5690;
    --panel: rgba(222, 226, 244, 0.72);
    --logo-bg: #0f1a45;
    --logo-accent: #8dc63f;
    --ink: #1f2a6b;
    --title: #e9ebf7;
  }
  * { margin: 0; padding: 0; box-sizing: border-box; }
  html, body { width: 1200px; height: 1000px; overflow: hidden; background: var(--navy-deep); }
  .poster {
    position: relative;
    width: 1200px;
    height: 1000px;
    overflow: hidden;
  }
  .scene-backdrop {
    position: absolute;
    inset: 0;
    background:
      radial-gradient(circle at 1070px 230px, rgba(220, 215, 240, 0.55) 0, rgba(220, 215, 240, 0) 260px),
      radial-gradient(circle at 470px 560px, var(--navy-deep) 0, rgba(30, 33, 96, 0.4) 460px, rgba(30, 33, 96, 0) 520px),
      linear-gradient(160deg, var(--navy-soft) 0%, var(--navy-mid) 45%, var(--wood-tint) 100%);
  }
  .info-panel {
    position: absolute;
    left: 326px;
    top: 133px;
    width: 545px;
    height: 545px;
    border-radius: 18px;
    background: var(--panel);
  }
  .festival-mark {
    position: absolute;
    left: 161px;
    top: 66px;
    width: 235px;
    height: 177px;
    background: var(--logo-bg);
    display: flex;
    align-items: center;
    justify-content: center;
    gap: 12px;
  }
  .festival-mark__dot {
    width: 22px;
    height: 22px;
    border-radius: 50%;
    background: var(--logo-accent);
  }
  .festival-mark__name {
    font-family: 'Josefin Sans', sans-serif;
    font-weight: 600;
    font-size: 36px;
    letter-spacing: 2px;
    color: #ffffff;
    padding-top: 6px;
  }
  .tagline {
    position: absolute;
    left: 0;
    top: 264px;
    width: 100%;
    text-align: center;
    font-family: 'Parisienne', cursive;
    font-size: 36px;
    line-height: 72px;
    letter-spacing: 2px;
    color: var(--ink);
  }
  .festival-title {
    position: absolute;
    left: 0;
    top: 750px;
    width: 100%;
    text-align: center;
    font-family: 'Josefin Sans', sans-serif;
    font-weight: 300;
    font-size: 44px;
    line-height: 67px;
    letter-spacing: 5px;
    color: var(--title);
  }
</style>
</head>
<body>
  <main class="poster">
    <div class="scene-backdrop" role="img" aria-label="Overhead photo of a vintage film reel and a spilled box of popcorn on a wooden table, tinted deep navy"></div>

    <section class="info-panel">
      <div class="festival-mark">
        <span class="festival-mark__dot"></span>
        <span class="festival-mark__name">HOCG</span>
      </div>
      <p class="tagline">
        Something for everyone<br>
        from around the world<br>
        7 - 13 September, 2017
      </p>
    </section>

    <h1 class="festival-title">
      20TH ANNUAL HARBORLINE<br>
      OPEN CINEMA GATHERING
    </h1>
  </main>
</body>
</html>
```